Gemstones e-commerce web-site needs a new template/style

We would like to highlight some of our more exclusive product (gemstones) in a new signature template that has its own style, fonts and colors. The new template would allow for larger and more detailed images. e.g. Tovelcrest.com. The design should account for different sized mobile devices. Current site is http://www.quarlinstonesusa.example

Industry/Entity Type

Product

Number of Pages Required

2 page

```html
<!DOCTYPE html>
<html lang="en">
<head>
<meta charset="utf-8">
<title>Quarlin Atelier – Home</title>
<link rel="stylesheet" href="https://fonts.googleapis.com/css2?family=Arimo:wght@400;700&display=swap">
<style>
  :root{
    --green:#169c48;
    --canvas:#f3f3f3;
    --white:#ffffff;
    --band:#dcdcdc;
    --muted:#8c8c8c;
    --field:#e9ebec;
    --ink:#4a4a4a;
  }
  *{box-sizing:border-box;margin:0;padding:0}
  html,body{width:1200px;height:1000px;overflow:hidden}
  body{background:var(--canvas);font-family:"Arimo",Arial,sans-serif;color:var(--ink)}
  .page{position:absolute;left:280px;top:18px;width:640px;height:964px;background:var(--white);box-shadow:0 2px 12px rgba(0,0,0,.12);overflow:hidden}

  /* header */
  .site-header{position:relative;height:111px}
  .brand{position:absolute;left:32px;top:30px}
  .brand-name{font-size:19px;font-weight:700;color:var(--ink);letter-spacing:-.2px;line-height:22px}
  .brand-tagline{font-size:10px;color:var(--ink);margin-top:1px}
  .account-links{position:absolute;right:42px;top:33px;font-size:7px;color:var(--muted);letter-spacing:.3px;word-spacing:4px}
  .search{position:absolute;right:38px;top:56px;width:108px;height:12px;border-radius:6px;background:var(--band)}
  .search svg{position:absolute;right:5px;top:2px}
  .main-nav{position:absolute;right:24px;top:92px;display:flex;gap:14px;font-size:7px;color:var(--green);text-transform:uppercase;letter-spacing:.2px}
  .main-nav .active{position:relative}
  .main-nav .active::after{content:"";position:absolute;left:-7px;right:-7px;top:11px;height:2px;background:var(--green)}

  /* hero */
  .hero{height:195px;background:
      radial-gradient(circle at 38% 40%,#6bbf74 0 8%,transparent 12%),
      radial-gradient(circle at 80% 70%,#e3b05a 0 12%,transparent 20%),
      radial-gradient(circle at 15% 45%,#c9a3cf 0 7%,transparent 12%),
      radial-gradient(circle at 34% 78%,#c86f76 0 8%,transparent 13%),
      radial-gradient(circle at 55% 60%,#4fa95a 0 6%,transparent 10%),
      radial-gradient(circle at 45% 8%,#6ea4d6 0 6%,transparent 10%),
      linear-gradient(180deg,#3a2f2c 0%,#9c8c86 25%,#e8dcd6 60%,#efe6e1 100%)}

  /* about */
  .about{height:102px;background:var(--band);text-align:center;padding-top:22px}
  .section-title{font-size:11px;color:var(--green);font-weight:400;letter-spacing:.2px}
  .about p{font-size:7px;line-height:15px;color:var(--muted);width:470px;margin:9px auto 0}

  /* products */
  .products{padding-top:27px;text-align:center}
  .product-grid{display:grid;grid-template-columns:repeat(4,130px);grid-auto-rows:93px;gap:16px 14px;margin:13px 0 0 39px}
  .product-tile{background:#e6e6e6}
  .tile-topaz{background:radial-gradient(circle at 45% 50%,#6fc2dc 0 35%,#2b7fa4 55%,#dedede 75%)}
  .tile-garnet-ring{background:radial-gradient(circle at 50% 45%,#e2782b 0 18%,#c9c9c9 34%,#e9e9e9 60%)}
  .tile-carving{background:radial-gradient(ellipse at 50% 55%,#4c56a6 0 38%,#d9d9df 66%)}
  .tile-earrings{background:linear-gradient(90deg,#e6e6e6,#b9a6cb 30%,#e6e6e6 50%,#b9a6cb 75%,#e6e6e6)}
  .tile-ruby-yellow{background:radial-gradient(circle at 55% 50%,#b3263c 0 24%,#d2b24c 40%,#ececec 62%)}
  .tile-ruby-rose{background:radial-gradient(circle at 45% 40%,#c42b4f 0 20%,#d7a48a 38%,#efefef 60%)}
  .tile-pink-ring{background:radial-gradient(circle at 55% 45%,#e08bc4 0 14%,#c6c6c6 30%,#ececec 58%)}
  .tile-red-gem{background:radial-gradient(ellipse at 50% 50%,#d0323a 0 30%,#7a1519 62%,#dadada 80%)}

  /* memberships */
  .memberships{position:absolute;left:0;right:0;top:740px;display:flex;justify-content:center;align-items:center;gap:34px}
  .badge{background:#e4e4e4}
  .badge-wide{width:82px;height:38px}
  .badge-round{width:50px;height:50px;border-radius:50%}
  .badge-fair{width:92px;height:42px}
  .badge-listing{width:92px;height:36px}

  /* footer */
  .site-footer{position:absolute;left:0;right:0;top:811px;height:153px;background:var(--green);color:var(--white)}
  .footer-col{position:absolute;top:18px;font-size:8px;line-height:11px}
  .footer-col h4{font-size:8px;font-weight:400;text-transform:uppercase;margin-bottom:4px}
  .col-nav{left:38px}
  .col-company{left:133px}
  .col-services{left:237px}
  .col-services ul{padding-left:2px}
  .footer-col ul{list-style:none}
  .shipping{position:absolute;left:355px;top:18px;display:flex;gap:4px;font-size:6.5px;line-height:8px;text-transform:uppercase;text-align:right}
  .contact{position:absolute;left:452px;top:12px;width:154px}
  .contact h4{font-size:12px;font-weight:400;margin-bottom:8px}
  .field{display:block;width:153px;height:15px;background:var(--field);margin-bottom:6px}
  .field-message{height:50px}
  .copyright{position:absolute;left:38px;top:124px;font-size:6.5px}
  .social{position:absolute;left:374px;top:118px;display:flex;gap:3px}
  .social span{width:13px;height:13px;border-radius:50%;background:var(--white)}
  .social span:nth-child(2){background:#dff2e6}
  .social span:nth-child(3){background:#f4c99a}
  .social span:nth-child(4){background:#3a3a3a}
</style>
</head>
<body>
<div class="page">
  <header class="site-header">
    <div class="brand">
      <div class="brand-name">Quarlin Atelier</div>
      <div class="brand-tagline">Clarity In Every Cut</div>
    </div>
    <div class="account-links">LOGIN REGISTER</div>
    <div class="search">
      <svg width="8" height="8" viewBox="0 0 8 8"><circle cx="3.2" cy="3.2" r="2.4" fill="none" stroke="#777" stroke-width="1"/><line x1="5" y1="5" x2="7.5" y2="7.5" stroke="#777" stroke-width="1"/></svg>
    </div>
    <nav class="main-nav">
      <span class="active">Home</span><span>Gemstone</span><span>Show</span><span>Special Gemstone</span><span>Carvings</span><span>Beads</span><span>Gold Jewelry</span><span>Silver Jewelry</span>
    </nav>
  </header>

  <div class="hero" role="img" aria-label="Assorted cut gemstones in green, gold, pink, violet and blue scattered on a pale surface"></div>

  <section class="about">
    <h2 class="section-title">ABOUT OUR COMPANY</h2>
    <p>"We intend to provide our customers with the best online shopping experience from beginning to end, with a smart, searchable website, easy-to-follow instructions, clear and secure payment methods, and fast, quality delivery."</p>
  </section>

  <section class="products">
    <h2 class="section-title">OUR PRODUCTS</h2>
    <div class="product-grid">
      <div class="product-tile tile-topaz" role="img" aria-label="Blue cushion-cut topaz"></div>
      <div class="product-tile tile-garnet-ring" role="img" aria-label="Orange gemstone ring with diamond halo"></div>
      <div class="product-tile tile-carving" role="img" aria-label="Blue carved gemstone figure"></div>
      <div class="product-tile tile-earrings" role="img" aria-label="Silver earrings and pendant with violet stones"></div>
      <div class="product-tile tile-ruby-yellow" role="img" aria-label="Oval ruby ring with yellow gold and diamonds"></div>
      <div class="product-tile tile-ruby-rose" role="img" aria-label="Ruby ring set in rose gold"></div>
      <div class="product-tile tile-pink-ring" role="img" aria-label="Pink sapphire ring with double diamond halo"></div>
      <div class="product-tile tile-red-gem" role="img" aria-label="Faceted oval red gemstone"></div>
    </div>
  </section>

  <div class="memberships">
    <div class="badge badge-wide" role="img" aria-label="Trade association membership badge"></div>
    <div class="badge badge-round" role="img" aria-label="Gem trade association member badge"></div>
    <div class="badge badge-fair" role="img" aria-label="Gem fair 2016 badge"></div>
    <div class="badge badge-listing" role="img" aria-label="Online marketplace store badge"></div>
  </div>

  <footer class="site-footer">
    <div class="footer-col col-nav">
      <ul><li>Home</li><li>Gemstone</li><li>Show</li><li>Special Gemstone</li><li>Carvings</li><li>Beads</li><li>Gold Jewelry</li><li>Silver Jewelry</li></ul>
    </div>
    <div class="footer-col col-company">
      <h4>The Company</h4>
      <ul><li>About Quarlin Atelier</li><li>Contact Us</li><li>FAQ's</li><li>Testimonials</li></ul>
    </div>
    <div class="footer-col col-services">
      <h4>The Services</h4>
      <ul><li>Policies</li><li>Privacy Policy</li><li>Site Map</li></ul>
    </div>
    <div class="shipping">
      <span>Free shipping<br>within the U.S.</span>
      <svg width="24" height="14" viewBox="0 0 24 14"><rect x="1" y="1" width="14" height="9" fill="none" stroke="#fff" stroke-width="1.2"/><path d="M15 4h4l3 3v3h-7z" fill="none" stroke="#fff" stroke-width="1.2"/><circle cx="5" cy="11.5" r="1.8" fill="#fff"/><circle cx="18" cy="11.5" r="1.8" fill="#fff"/></svg>
    </div>
    <div class="contact">
      <h4>CONTACT US</h4>
      <span class="field"></span>
      <span class="field"></span>
      <span class="field field-message"></span>
    </div>
    <div class="social"><span></span><span></span><span></span><span></span></div>
    <p class="copyright">© 2016. Quarlin Atelier | All Rights Reserved.</p>
  </footer>
</div>
</body>
</html>
```